Business Card Design

We need elegant business card design. We are conglomerate for different businesses. Nature of our businesses include Construction, Health care, Energy and Automotive

Target Market(s)

Business to business clients ages 40+

Industry/Entity Type

Automotive

Contact Information for Business Card

Tariq (Ted) Nadeem
CEO
Brightvale Group of Companies, Inc
7314 Ridgeline Rd S, Houston, TX, 77391
C:832-555-4173 O: 281-555-3806 F: 281-555-9152

```html
<!DOCTYPE html>
<html lang="en">
<head>
<meta charset="utf-8">
<title>Brightvale Group of Companies – Business Card</title>
<link rel="stylesheet" href="https://fonts.googleapis.com/css2?family=Oxanium:wght@500&display=swap">
<style>
  :root {
    --card-black: #0b0b0b;
    --ink-light: #e4e4e4;
    --rule-light: #d8d8d8;
  }
  html, body {
    margin: 0;
    padding: 0;
    width: 1200px;
    height: 758px;
    overflow: hidden;
    background: var(--card-black);
  }
  .business-card {
    position: relative;
    width: 1200px;
    height: 758px;
    background: var(--card-black);
    color: var(--ink-light);
    font-family: "Oxanium", sans-serif;
    font-weight: 500;
    text-transform: uppercase;
    display: flex;
    flex-direction: column;
    align-items: center;
  }
  .company-name {
    margin-top: 210px;
    text-align: center;
    font-size: 34px;
    letter-spacing: 4px;
    line-height: 1.35;
    color: var(--ink-light);
  }
  .holder-name {
    margin-top: 92px;
    font-size: 30px;
    letter-spacing: 2px;
    padding: 0 30px 14px;
    border-bottom: 3px solid var(--rule-light);
  }
  .address {
    margin-top: 22px;
    font-size: 26px;
    letter-spacing: 2px;
  }
  .contact-row {
    margin-top: 24px;
    display: flex;
    gap: 52px;
    font-size: 26px;
    letter-spacing: 2px;
  }
  .contact-item {
    display: flex;
    align-items: center;
    gap: 12px;
  }
  .contact-icon {
    width: 26px;
    height: 26px;
    fill: none;
    stroke: var(--ink-light);
    stroke-width: 2;
  }
  .contact-icon .solid { fill: var(--ink-light); stroke: none; }
</style>
</head>
<body>
  <main class="business-card">
    <h1 class="company-name">Brightvale<br>Group of Companies, Inc</h1>

    <p class="holder-name">Tariq (Ted) Nadeem</p>
    <p class="address">7314 Ridgeline Rd S, Houston, TX, 77391</p>

    <div class="contact-row">
      <span class="contact-item">
        <svg class="contact-icon" viewBox="0 0 26 26" aria-hidden="true">
          <rect x="7" y="2" width="12" height="22" rx="2"/>
          <line x1="11" y1="20" x2="15" y2="20"/>
        </svg>
        832-555-4173
      </span>
      <span class="contact-item">
        <svg class="contact-icon" viewBox="0 0 26 26" aria-hidden="true">
          <path class="solid" d="M6 3 L10 3 L12 9 L9 11 Q12 17 15 18 L17 15 L23 17 L23 21 Q22 24 18 23 Q6 19 3 7 Q3 3 6 3 Z"/>
        </svg>
        832-555-4173
      </span>
      <span class="contact-item">
        <svg class="contact-icon" viewBox="0 0 26 26" aria-hidden="true">
          <rect class="solid" x="2" y="10" width="22" height="12" rx="2"/>
          <rect x="7" y="3" width="12" height="7"/>
        </svg>
        281-555-9152
      </span>
    </div>
  </main>
</body>
</html>
```